Business Recognition Design

We need a design for a recognition to be given to business leaders in our community.
The recognition shall be made on a brass plaque on wood panel background (picture attached, please use it as a background), and all drawing must be in vectors and only one color (black).
It should also have a logo on the top and signature on the right bottom.
The text is enclosed in DOC file.
Updates

Reason: just to be able to find the best solution

Reason: None of the suggestion is good enough. Logo in general is too big in comparison with the rest of the plate.

Industry/Entity Type

Business

Requirements
Must have
• - standard Windows font (or possibility to install the same font on Windows), as the name on the recognition shall be printed in the same font
Nice to have
• - some graphic element (in curves) representing achievements in business
- should look great :)

```html
<!DOCTYPE html>
<html lang="de">
<head>
<meta charset="utf-8">
<title>Auszeichnung – Unternehmer Deutschlands 2013</title>
<link href="https://fonts.googleapis.com/css2?family=Arimo:wght@400;700&display=swap" rel="stylesheet">
<style>
  :root {
    --backdrop: #3a3a3a;
    --wood-dark: #4e2f19;
    --wood-mid: #6e4527;
    --wood-light: #85583a;
    --brass-dark: #c29a2e;
    --brass-mid: #e6c55a;
    --brass-light: #f6e08a;
    --engrave: #111111;
    --screw-dark: #8a6a14;
    --screw-light: #f3d46a;
  }
  html, body {
    margin: 0;
    width: 1200px;
    height: 832px;
    overflow: hidden;
    background: var(--backdrop);
    font-family: "Arimo", Arial, sans-serif;
  }
  .wood-panel {
    position: absolute;
    left: 165px;
    top: 81px;
    width: 870px;
    height: 670px;
    background: linear-gradient(90deg, var(--wood-dark), var(--wood-mid) 30%, var(--wood-light) 55%, var(--wood-mid) 80%, var(--wood-dark));
    border-radius: 3px;
    box-shadow: inset 0 0 0 3px rgba(0,0,0,0.25);
  }
  .brass-plate {
    position: absolute;
    left: 38px;
    top: 30px;
    right: 38px;
    bottom: 34px;
    background: linear-gradient(100deg, var(--brass-dark), var(--brass-mid) 25%, var(--brass-light) 50%, var(--brass-mid) 75%, var(--brass-dark));
    color: var(--engrave);
    box-shadow: 0 2px 4px rgba(0,0,0,0.4);
  }
  .screw {
    position: absolute;
    width: 18px;
    height: 18px;
    border-radius: 50%;
    background: radial-gradient(circle at 35% 35%, var(--screw-light), var(--screw-dark));
  }
  .screw.tl { left: 14px; top: 14px; }
  .screw.tr { right: 14px; top: 14px; }
  .screw.bl { left: 14px; bottom: 14px; }
  .screw.br { right: 14px; bottom: 14px; }
  .plate-text { position: absolute; left: 64px; margin: 0; white-space: nowrap; }
  .brand-name { top: 92px; font-size: 36px; font-weight: 700; letter-spacing: -0.5px; }
  .award-title { top: 156px; font-size: 36px; font-weight: 400; }
  .award-line { font-size: 28px; font-weight: 700; }
  .award-line.first { top: 201px; }
  .award-line.second { top: 243px; }
  .award-for { top: 284px; font-size: 19px; }
  .recipient { top: 310px; font-size: 26px; font-weight: 700; }
  .body-copy { top: 346px; font-size: 17px; line-height: 30px; }
  .body-copy strong { font-size: 20px; }
  .body-copy small { font-size: 11px; font-weight: 700; }
  .signature-line { top: 542px; font-size: 18px; }
  .achievement-chart {
    position: absolute;
    left: 500px;
    top: 125px;
    width: 270px;
    height: 431px;
  }
</style>
</head>
<body>
  <div class="wood-panel">
    <div class="brass-plate">
      <span class="screw tl"></span><span class="screw tr"></span>
      <span class="screw bl"></span><span class="screw br"></span>

      <p class="plate-text brand-name">TrustLedger</p>
      <p class="plate-text award-title">AUSZEICHNUNG</p>
      <p class="plate-text award-line first">als herausragendster</p>
      <p class="plate-text award-line second">Unternehmer Deutschlands 2013</p>
      <p class="plate-text award-for">für</p>
      <p class="plate-text recipient">Herrn Dipl.-Kfm. Karl Beispiel</p>
      <p class="plate-text body-copy">
        Unter der Leitung von <strong>Herr Dipl.-Kfm.</strong> <small>Karl Beispiel</small><br>
        hat sich die FIRMA GmbH im Jahr 2013 unter<br>
        den ersten 5% der größten deutschen<br>
        Wirtschaftsunternehmen platziert.
      </p>
      <p class="plate-text signature-line">Gilching, 20. Juni 2013 Lena Hofmann</p>

      <svg class="achievement-chart" viewBox="0 0 270 431" aria-hidden="false">
        <rect x="0" y="281" width="73" height="150" fill="#111"/>
        <rect x="84" y="254" width="73" height="177" fill="#111"/>
        <rect x="170" y="214" width="74" height="217" fill="#111"/>
        <rect x="145" y="0" width="125" height="214" fill="#111" opacity="0.85" role="img" aria-label="Silhouette einer jubelnden Person mit erhobenen Armen auf dem höchsten Balken"/>
      </svg>
    </div>
  </div>
</body>
</html>
```